The Nine Gates for Tablet Reliance - Contemporary Book Cover Design

The Nine Gates for Tablet Reliance was published in March 2019 and is available on Brimora and other platforms now. However, I am not happy with the cover.  It's a good design in some ways - I thought it would stand out and be easily recognizable. But I don't really like the color scheme and feel that a self-help book should probably use some lighter colors and that the red is too strident. The color scheme carries over into other marketing materials like the website, social media, etc. and I don't like the red and black scheme for these purposes.
It's not essential that the cover contain an endorsement like the current one but it could. Here are some endorsements:
“A must-read for anyone who is addicted to or thinks they may have a problem with digital technology. This eloquent work will also be useful to academics and clinicians exploring potential solutions. The author recognizes the similarities between smartphone addiction and other addictions, and logically applies one of the most effective known solutions for addiction - The Nine Gates.”
-- Dale Wickersham: Noted Interventionist, Keynote Speaker and Addiction Visionary
“If you suffer from digital addiction, I strongly encourage you to use this book as your road map to get you back to the real world.”
-- Thomas Quillard, Founder of Online Channel Monitor.
The back cover would have the new design / color scheme, but can have similar text, bio, author image, etc. Or we could include the endorsements there and shorten the other text.
As for the cover it could be stylized, or an image, a partial image, or whatever. I am open to suggestions. Think about what would be inviting for a person searching for help with moderating their smartphone use.
Let's add a subtitle as well "An Inner Journey to Balanced Tablet Habits"
Here is a link to the book:
https://www.brimora.example/Nine-Gates-Tablet-Reliance/dp/4086213590

Target Market(s)
General, since this issue affects almost everyone.
Colors
Designer to choose colors to be used in the design.
Look and feel

```html
<!DOCTYPE html>
<html lang="en">
<head>
<meta charset="utf-8">
<title>The Nine Gates for Tablet Reliance – Cover Spread</title>
<link rel="stylesheet" href="https://fonts.googleapis.com/css2?family=Lato:wght@900&family=Montserrat:ital,wght@0,400;0,500;0,700;1,400&display=swap">
<style>
  :root {
    --bg: #4a0f55;
    --orange: #ef7a22;
    --orange-deep: #e8661a;
    --orange-light: #f4a060;
    --cream: #f6d6a8;
    --purple: #6b3a83;
    --purple-panel: #5b2a6c;
    --white: #ffffff;
    --photo-tone: #b77b52;
  }
  * { margin: 0; padding: 0; box-sizing: border-box; }
  html, body { width: 1200px; height: 818px; overflow: hidden; }
  body {
    background: var(--bg);
    font-family: "Montserrat", sans-serif;
    display: flex; align-items: center; justify-content: center;
  }
  .spread { display: flex; height: 735px; box-shadow: 0 12px 40px rgba(0,0,0,.35); }

  /* Back cover */
  .back-cover {
    width: 490px; height: 100%;
    background: linear-gradient(100deg, #d9783a 0%, #e58b48 30%, #d27034 55%, #e89152 80%, #d47438 100%);
    padding: 40px 34px 70px;
  }
  .back-panel {
    height: 100%;
    background: var(--purple-panel);
    color: var(--white);
    padding: 30px 28px 24px;
    display: flex; flex-direction: column;
  }
  .back-lead { font-size: 15px; line-height: 1.3; font-weight: 500; margin-bottom: 14px; }
  .back-body { font-size: 10.5px; line-height: 1.42; margin-bottom: 10px; }
  .about { display: flex; gap: 16px; margin-top: auto; }
  .author-photo {
    flex: 0 0 150px; height: 140px;
    background: linear-gradient(135deg, #6f7a3a, #9a7a5a 50%, #3c3530);
    border: 3px solid var(--white);
  }
  .about-heading { font-size: 11px; font-weight: 700; letter-spacing: .03em; margin-bottom: 6px; }
  .about-body { font-size: 10.5px; line-height: 1.42; }

  /* Spine */
  .spine { width: 40px; height: 100%; background: linear-gradient(90deg, var(--orange-deep), var(--orange), var(--orange-deep)); }

  /* Front cover */
  .front-cover { position: relative; width: 490px; height: 100%; overflow: hidden; }
  .cover-photo {
    position: absolute; inset: 0;
    background:
      linear-gradient(150deg, transparent 45%, rgba(246,214,168,.85) 62%, var(--cream) 78%, rgba(246,214,168,.6) 92%),
      linear-gradient(160deg, var(--orange) 0%, var(--orange-light) 55%, var(--photo-tone) 100%);
  }
  .title {
    position: absolute; top: 42px; right: 30px;
    font-family: "Lato", sans-serif; font-weight: 900;
    font-size: 74px; line-height: .9; text-align: right;
    color: var(--white); text-transform: uppercase;
  }
  .title .accent { color: var(--purple); }
  .subtitle {
    position: absolute; top: 400px; right: 34px; width: 330px;
    font-family: "Lato", sans-serif; font-weight: 900;
    font-size: 19px; line-height: 1.15; text-align: right;
    color: var(--purple); text-transform: uppercase;
  }
  .author-name {
    position: absolute; bottom: 38px; left: 34px;
    font-family: "Lato", sans-serif; font-weight: 900;
    font-size: 30px; letter-spacing: .02em;
    color: var(--purple); text-transform: uppercase;
  }
</style>
</head>
<body>
  <main class="spread">
    <section class="back-cover">
      <div class="back-panel">
        <p class="back-lead">An Effective Solution to the challenge of Smartphone addiction based on the rich and successful tradition of the nine gates.</p>
        <p class="back-body">The nine gates are one of the most effective methods for treating addiction in human history. Originating with Sober Circle Fellowship in 1939, The Nine Gates have since been used to treat a variety of other addictions, including drugs, sex, gambling, eating disorders and many others. Now in this groundbreaking work The Nine Gates are applied to the complex and evolving contemporary phenomenon of Smartphone Addiction.</p>
        <p class="back-body">Smartphone Addiction is a new and troubling phenomenon that has burst upon an unprepared society with alarming speed. Many people crave the use of Smartphone Technology and its constant and effective system of sensory rewards in a strikingly similar way to any other addiction. Smartphones and the complex software they run have been architected to promote continued and progressive usage. This sophisticated technology clearly feeds on natural addictive tendencies, and recent evidence suggests Smartphones are intentionally designed to be addictive.</p>
        <div class="about">
          <div class="author-photo" role="img" aria-label="Portrait photograph of the author"></div>
          <div>
            <h2 class="about-heading">ABOUT THE AUTHOR</h2>
            <p class="about-body">Jonah Sorrel is a Digital Marketing Consultant with many years of professional coding and consulting experience. He also struggled with addiction to drugs and alcohol and is now clean and sober in a Nine-Gate program for over 15 years. This unique combination of Nine-Gate experience and technology expertise led him to create The Nine Gates for Tablet Reliance.</p>
          </div>
        </div>
      </div>
    </section>

    <div class="spine"></div>

    <section class="front-cover">
      <div class="cover-photo" role="img" aria-label="Photograph of a curving staircase with a railing in warm orange and cream light"></div>
      <h1 class="title">The <span class="accent">Nine</span><br><span class="accent">Gates</span> for<br>Tablet<br>Reliance</h1>
      <p class="subtitle">An Inner Journey to Balanced Tablet Habits</p>
      <p class="author-name">Jonah Sorrel</p>
    </section>
  </main>
</body>
</html>
```